Club Lumora - Dermatology Consultation App

Club Lumora is launching a new Quince QWS App for online Dermatology consultation. We would appreciate a simple Scandinavian design which communicates trust, comfort and expensive feel. Most yacht designs have similar color palette, light wood colors and textures, but don’t be restricted by those in your artistic search.
The process is completed in three easy steps:
1. take a Snapshot.
2. Describe and Send it.
3. get Diagnosis and Treatment.
The Home screen should also have buttons - Start new Case, Follow up Visit, Rx Refill.
15% of the Home screen should also have a field/button - Medical Cosmetics Shop.
10% of the Home screen should also have a field or buttons for Our Partners (sponsors) – Talvine, Norelisa, Parlo, Ostra. (if you click you would be directed to their sites)
Note / Suggestion : Maybe you could use a larger picture of a dermatologist and have overlying fields and content, just for more influencing effect. (I am not a professional though)
Thank you so much.
Updates
Target Market(s)
24 - 59 Female
Industry/Entity Type
Club
Look and feel

```html
<!DOCTYPE html>
<html lang="en">
<head>
<meta charset="utf-8">
<title>Club Lumora – Home</title>
<link rel="stylesheet" href="https://fonts.googleapis.com/css2?family=Figtree:wght@300;400;500&display=swap">
<style>
  :root {
    --page-bg: #41354f;
    --screen-top: #4f4a44;
    --screen-mid: #3a2c24;
    --screen-low: #1e1612;
    --screen-base: #0c0807;
    --gold: #c09a5b;
    --gold-line: #8c6e47;
    --text-light: #f1ece6;
    --teal: #27645a;
    --rose: #a93c52;
    --amber: #b7862f;
    --btn-fill: rgba(40, 30, 24, 0.55);
    --btn-fill-dark: rgba(14, 10, 8, 0.7);
  }
  * { box-sizing: border-box; margin: 0; padding: 0; }
  html, body { width: 960px; height: 1200px; overflow: hidden; }
  body {
    background: var(--page-bg);
    font-family: "Figtree", "Helvetica Neue", Arial, sans-serif;
    color: var(--text-light);
  }
  .app-screen {
    position: absolute;
    left: 140px; top: 0;
    width: 680px; height: 1200px;
    overflow: hidden;
    background: var(--screen-base);
  }
  .hero-backdrop {
    position: absolute; inset: 0 0 370px 0;
    background:
      radial-gradient(ellipse 60% 40% at 70% 45%, rgba(120, 80, 60, 0.55), transparent 70%),
      radial-gradient(ellipse 50% 35% at 25% 60%, rgba(90, 70, 55, 0.5), transparent 70%),
      linear-gradient(180deg, var(--screen-top) 0%, var(--screen-mid) 55%, var(--screen-low) 100%);
  }
  .lower-panel {
    position: absolute; left: 0; right: 0; top: 830px; bottom: 0;
    background: linear-gradient(180deg, var(--screen-low) 0%, var(--screen-base) 100%);
  }
  .status-bar {
    position: absolute; top: 0; left: 0; right: 0; height: 50px;
    display: flex; align-items: center; justify-content: space-between;
    padding: 0 18px; font-size: 24px; font-weight: 400;
  }
  .status-left, .status-right { display: flex; align-items: center; gap: 8px; }
  .brand {
    position: absolute; top: 130px; left: 0; right: 0;
    display: flex; align-items: center; justify-content: center; gap: 22px;
    color: var(--gold); font-size: 78px; font-weight: 500; letter-spacing: 1px;
  }
  .brand-dot {
    width: 46px; height: 46px; border-radius: 50%;
    border: 3px solid var(--gold);
  }
  .action-btn, .link-btn {
    position: absolute; left: 58px; width: 565px; height: 120px;
    border: 3px solid var(--gold-line);
    display: flex; align-items: center;
    font-size: 38px; font-weight: 300; letter-spacing: 0.5px;
  }
  .action-btn { background: var(--btn-fill); }
  .action-icon {
    width: 112px; height: 100%;
    display: flex; align-items: center; justify-content: center;
  }
  .action-icon.new { background: var(--teal); }
  .action-icon.follow { background: var(--rose); }
  .action-icon.refill { background: var(--amber); }
  .action-label { padding-left: 32px; }
  .link-btn { justify-content: center; background: var(--btn-fill-dark); }
</style>
</head>
<body>
<main class="app-screen">
  <div class="hero-backdrop" role="img" aria-label="Soft blurred photo of a dermatologist in a warm-toned clinic"></div>
  <div class="lower-panel"></div>

  <header class="status-bar">
    <div class="status-left">
      <svg width="74" height="16" viewBox="0 0 74 16" aria-hidden="true">
        <g fill="#f1ece6"><circle cx="7" cy="8" r="6"/><circle cx="22" cy="8" r="6"/><circle cx="37" cy="8" r="6"/><circle cx="52" cy="8" r="6"/></g>
        <circle cx="67" cy="8" r="5.2" fill="none" stroke="#f1ece6" stroke-width="1.5"/>
      </svg>
      <span>VERANO</span>
      <svg width="30" height="22" viewBox="0 0 30 22" aria-hidden="true" fill="none" stroke="#f1ece6" stroke-width="3" stroke-linecap="round">
        <path d="M3 8a17 17 0 0 1 24 0"/><path d="M8 13a10 10 0 0 1 14 0"/><circle cx="15" cy="18" r="2" fill="#f1ece6" stroke="none"/>
      </svg>
    </div>
    <div class="status-right">
      <svg width="14" height="22" viewBox="0 0 14 22" aria-hidden="true" fill="none" stroke="#bbb" stroke-width="1.6">
        <path d="M2 6l10 9-5 5V2l5 5L2 16"/>
      </svg>
      <span>82%</span>
      <svg width="66" height="22" viewBox="0 0 66 22" aria-hidden="true">
        <rect x="1" y="2" width="48" height="18" rx="3" fill="none" stroke="#f1ece6" stroke-width="1.5"/>
        <rect x="4" y="5" width="36" height="12" rx="1.5" fill="#f1ece6"/>
        <rect x="51" y="8" width="3" height="6" fill="#f1ece6"/>
        <path d="M62 3l-5 9h4l-2 8 6-10h-4z" fill="#f1ece6"/>
      </svg>
    </div>
  </header>

  <div class="brand">
    <span class="brand-dot"></span>
    <span>club lumora</span>
  </div>

  <a class="action-btn" style="top:346px">
    <span class="action-icon new">
      <svg width="76" height="76" viewBox="0 0 76 76" aria-hidden="true" fill="none" stroke="#fff" stroke-width="3">
        <circle cx="38" cy="38" r="34"/><path d="M38 22v32M22 38h32"/>
      </svg>
    </span>
    <span class="action-label">START NEW CASE</span>
  </a>

  <a class="action-btn" style="top:501px">
    <span class="action-icon follow">
      <svg width="80" height="84" viewBox="0 0 80 84" aria-hidden="true" fill="none" stroke="#fff" stroke-width="3">
        <path d="M56 16A34 34 0 0 0 8 48"/>
        <path d="M8 48a34 34 0 0 0 66-8" stroke-dasharray="7 6"/>
        <path d="M46 6l12 10-12 8"/>
      </svg>
    </span>
    <span class="action-label">FOLLOW UP VISIT</span>
  </a>

  <a class="action-btn" style="top:663px">
    <span class="action-icon refill">
      <svg width="80" height="76" viewBox="0 0 80 76" aria-hidden="true" fill="none" stroke="#fff" stroke-width="3" stroke-linejoin="round">
        <path d="M28 30l26-16 16 26-26 16z"/>
        <path d="M54 14l8-5 8 14-8 5"/>
        <path d="M14 50c-6 6-6 12 0 12s6-6 0-12z"/>
      </svg>
    </span>
    <span class="action-label">Rx REFILL</span>
  </a>

  <a class="link-btn" style="top:880px">MEDICAL COSMETICS SHOP</a>
  <a class="link-btn" style="top:1032px">OUR PARTNERS</a>
</main>
</body>
</html>
```